Oversized Post card design

Need a post card design for rebrand, old post card attached for reference but some new content logos and colors. Id like to see new designs please use the one i posted as a reference of the type of design we like

Requirements
Must have
• Pricing page should no longer have "metered" plans only unlimited with these:
• 1 User: $29.99
• 2-10: $24.99/user
• 11-49: $21.99/user
• 50+: Contact Us!
• Add Ons:
• Call Recording: Starting at $5/user
• Additional Local Numbers: $1.99/number
• Fax to email: Starting at $8/user
• Toll Free Numbers: 1.99/number plus usage

```html
<!DOCTYPE html>
<html lang="en">
<head>
<meta charset="utf-8">
<title>Nimbra – Plans and Pricing Postcard</title>
<link href="https://fonts.googleapis.com/css2?family=Source+Sans+3:wght@400;600;700&display=swap" rel="stylesheet">
<style>
  :root{
    --purple:#6a3093;
    --blue:#139fdb;
    --cyan:#35c0e0;
    --grey:#b3b3b5;
    --grey-light:#dcdce0;
    --ink:#333;
    --white:#fff;
    --backdrop:#e9e9ec;
  }
  *{box-sizing:border-box;margin:0;padding:0}
  html,body{width:1000px;height:1200px;overflow:hidden;background:var(--backdrop);font-family:"Source Sans 3",Arial,sans-serif}
  .postcard{position:absolute;left:50px;width:900px;height:580px;background:var(--white);overflow:hidden;box-shadow:0 3px 10px rgba(0,0,0,.25)}
  .postcard--pricing{top:15px}
  .postcard--features{top:605px}
  .abs{position:absolute}
  .city-backdrop{position:absolute;inset:0;background:linear-gradient(135deg,#f2f2f4 0%,#cfcfd4 45%,#e6e6ea 70%,#bfc0c6 100%)}
  .chevron-art{position:absolute;left:0;top:0}
  .brand{position:absolute;left:80px;top:38px;display:flex;align-items:center;gap:8px;color:var(--purple);font-weight:700;font-size:24px;letter-spacing:2px}
  .brand__mark{width:16px;height:16px;background:var(--blue)}
  .title{left:100px;top:125px;width:300px;text-align:center;color:var(--purple);font-weight:700;font-size:44px;line-height:48px}
  .seat-heading{left:565px;top:50px;color:var(--purple);font-weight:700;font-size:27px}
  .price-table{left:570px;top:100px;width:262px}
  .price-row{display:flex;height:36px;margin-bottom:5px;background:var(--white);border:2px solid #888;border-top:none;border-left:none;align-items:center}
  .price-row__seats{width:118px;padding-left:6px;font-weight:700;font-size:19px;color:var(--ink);white-space:nowrap}
  .price-row__cost{flex:1;display:flex;align-items:center;gap:8px;font-size:17px;color:var(--ink)}
  .price-row__cost b{color:var(--blue);font-size:20px;font-weight:700}
  .price-row__cost sup{font-size:10px}
  .price-row__cost .contact{font-weight:700;font-size:17px;margin-left:28px}
  .addons-band{left:0;top:306px;width:900px;height:204px;background:var(--blue);box-shadow:0 4px 6px rgba(0,0,0,.25)}
  .addons-heading{left:70px;top:22px;color:var(--white);font-weight:700;font-size:29px}
  .addon{position:absolute;height:40px;display:flex;align-items:center}
  .addon__icon{width:40px;height:40px;background:var(--purple);display:flex;align-items:center;justify-content:center;margin-right:8px}
  .addon__box{height:40px;width:330px;background:var(--white);display:flex;align-items:center;font-weight:700;font-size:14.5px;overflow:hidden}
  .addon__name{color:var(--purple);padding-left:8px;width:184px;flex:none;white-space:nowrap}
  .addon__name--short{width:144px}
  .addon__price{flex:1;color:var(--blue);display:flex;align-items:center;gap:3px;white-space:nowrap;letter-spacing:-.1px}
  .addon__price svg{flex:none}
  .addon__price strong{color:#222}
  .contact-band{position:absolute;left:0;width:900px;height:36px;display:flex;align-items:center;justify-content:center;gap:32px;color:var(--white);font-weight:700;font-size:21px}
  .contact-band--purple{top:528px;background:var(--purple)}
  .contact-band--cyan{top:528px;background:var(--cyan)}
  .features-top{position:absolute;left:0;top:0;width:900px;height:329px}
  .headline{left:526px;top:30px;color:var(--purple);font-weight:700}
  .headline small{display:block;font-size:18px}
  .headline span{display:block;font-size:32px;line-height:34px}
  .cloud-art{left:480px;top:105px;width:400px;height:200px;border-radius:90px 100px 60px 60px;background:radial-gradient(circle at 50% 40%,#ffffff 0%,#f4f6f9 70%,#e9edf2 100%)}
  .service{position:absolute;left:30px;width:268px;text-align:right;color:var(--purple);font-size:13px;line-height:15px}
  .service h3{font-size:14.5px;font-weight:700;margin-bottom:1px}
  .service-icon{position:absolute;left:314px;width:42px;height:42px;border-radius:50%;background:var(--white);box-shadow:0 1px 3px rgba(0,0,0,.3)}
  .feature-list{position:absolute;top:342px;width:400px}
  .feature-list--left{left:70px}
  .feature-list--right{left:480px}
  .feature{margin-bottom:8px;font-size:13.5px;line-height:13px;color:#555}
  .feature h4{color:var(--blue);font-weight:700;font-size:14.5px;line-height:14px}
  .footer-strip{position:absolute;left:0;top:564px;width:900px;height:16px;background:linear-gradient(90deg,#d6d6da,#eeeef0,#cfd0d5)}
</style>
</head>
<body>

<section class="postcard postcard--pricing">
  <div class="city-backdrop" role="img" aria-label="Faded photo of glass office towers"></div>
  <svg class="chevron-art" width="900" height="306" viewBox="0 0 900 306">
    <polygon points="500,0 900,0 900,306 535,306 390,153" fill="var(--purple)"/>
    <polygon points="565,0 900,0 900,306 580,306 450,153" fill="var(--grey)" stroke="var(--grey)" stroke-width="14" stroke-linejoin="round"/>
  </svg>

  <div class="brand"><span class="brand__mark"></span>NIMBRA</div>
  <h1 class="abs title">PLANS<br>AND PRICING</h1>

  <h2 class="abs seat-heading">UNLIMITED SEAT</h2>
  <div class="abs price-table">
    <div class="price-row"><span class="price-row__seats">1 Users</span><span class="price-row__cost"><svg width="10" height="34"><polyline points="9,1 2,17 9,33" fill="none" stroke="var(--purple)" stroke-width="3"/></svg><b>$29<sup>.99</sup></b>/user</span></div>
    <div class="price-row"><span class="price-row__seats">2 - 10 &nbsp;Users</span><span class="price-row__cost"><svg width="10" height="34"><polyline points="9,1 2,17 9,33" fill="none" stroke="var(--purple)" stroke-width="3"/></svg><b>$24<sup>.99</sup></b>/user</span></div>
    <div class="price-row"><span class="price-row__seats">11 - 49 Users</span><span class="price-row__cost"><svg width="10" height="34"><polyline points="9,1 2,17 9,33" fill="none" stroke="var(--purple)" stroke-width="3"/></svg><b>$21<sup>.99</sup></b>/user</span></div>
    <div class="price-row"><span class="price-row__seats">50 + Users</span><span class="price-row__cost"><svg width="10" height="34"><polyline points="9,1 2,17 9,33" fill="none" stroke="var(--purple)" stroke-width="3"/></svg><span class="contact">Contact Us!</span></span></div>
  </div>

  <div class="abs addons-band">
    <h2 class="abs addons-heading">ADD ONS</h2>

    <div class="addon" style="left:70px;top:68px">
      <span class="addon__icon"><svg width="22" height="28" viewBox="0 0 22 28"><rect x="7" y="1" width="8" height="15" rx="4" fill="#fff"/><path d="M3 12a8 8 0 0 0 16 0M11 20v6M6 26h10" fill="none" stroke="#fff" stroke-width="2"/></svg></span>
      <div class="addon__box"><span class="addon__name">Call Recording</span><span class="addon__price"><svg width="10" height="38"><polyline points="9,1 2,19 9,37" fill="none" stroke="var(--purple)" stroke-width="3"/></svg><span>Starting at <strong>$5</strong>/user</span></span></div>
    </div>
    <div class="addon" style="left:70px;top:121px">
      <span class="addon__icon"><svg width="28" height="28" viewBox="0 0 28 28"><circle cx="14" cy="14" r="12" fill="none" stroke="#fff" stroke-width="2"/><path d="M10 8l3 3-2 2c1 2 2 3 4 4l2-2 3 3-2 2c-5 0-10-5-10-10z" fill="#fff"/></svg></span>
      <div class="addon__box"><span class="addon__name">Additional Local Numbers</span><span class="addon__price"><svg width="10" height="38"><polyline points="9,1 2,19 9,37" fill="none" stroke="var(--purple)" stroke-width="3"/></svg><span><strong>$1.99</strong>/number</span></span></div>
    </div>
    <div class="addon" style="left:452px;top:68px">
      <span class="addon__icon"><svg width="26" height="28" viewBox="0 0 26 28"><rect x="2" y="8" width="5" height="18" fill="#fff"/><rect x="9" y="2" width="14" height="24" fill="none" stroke="#fff" stroke-width="2"/><path d="M12 14h2M16 14h2M12 18h2M16 18h2M12 22h2M16 22h2" stroke="#fff" stroke-width="2"/></svg></span>
      <div class="addon__box"><span class="addon__name addon__name--short">Fax to email</span><span class="addon__price"><svg width="10" height="38"><polyline points="9,1 2,19 9,37" fill="none" stroke="var(--purple)" stroke-width="3"/></svg><span>Starting at <strong>$8</strong>/user</span></span></div>
    </div>
    <div class="addon" style="left:452px;top:121px">
      <span class="addon__icon"><svg width="28" height="28" viewBox="0 0 28 28"><circle cx="14" cy="14" r="12" fill="none" stroke="#fff" stroke-width="2"/><path d="M9 7l3 3-2 2c1 2 3 4 5 5l2-2 3 3-2 3c-6 0-11-5-11-11z" fill="#fff"/></svg></span>
      <div class="addon__box"><span class="addon__name addon__name--short">Toll Free Number</span><span class="addon__price"><svg width="10" height="38"><polyline points="9,1 2,19 9,37" fill="none" stroke="var(--purple)" stroke-width="3"/></svg><span><strong>$1.99</strong>/number plus usage</span></span></div>
    </div>
  </div>

  <div class="contact-band contact-band--purple"><span>corvalink.com</span><span>|</span><span>855.CORVAL1</span><span>|</span><span>sales@corvalink.com</span></div>
</section>

<section class="postcard postcard--features">
  <div class="features-top">
    <div class="city-backdrop" role="img" aria-label="Faded photo of glass office towers"></div>
    <svg class="chevron-art" width="900" height="329" viewBox="0 0 900 329">
      <polygon points="505,0 900,0 900,329 540,329 355,165" fill="var(--purple)"/>
      <polygon points="560,0 900,0 900,329 575,329 420,165" fill="var(--grey)" stroke="var(--grey)" stroke-width="14" stroke-linejoin="round"/>
    </svg>
    <div class="brand"><span class="brand__mark"></span>NIMBRA</div>

    <div class="service" style="top:118px"><h3>HOSTED PBX</h3>Innovative features, geo-redundant network,<br>jaw dropping price.</div>
    <div class="service-icon" style="top:120px"><svg width="42" height="42"><circle cx="21" cy="21" r="13" fill="none" stroke="var(--blue)" stroke-width="1.5"/><circle cx="21" cy="21" r="3" fill="var(--blue)"/></svg></div>
    <div class="service" style="top:185px"><h3>SIP TRUNKING</h3>Not ready to give up your current phone system?<br>Leverage the cloud for your phone service and<br>integrate seamlessly.</div>
    <div class="service-icon" style="top:191px"><svg width="42" height="42"><circle cx="21" cy="21" r="14" fill="none" stroke="var(--blue)" stroke-width="1.5"/><circle cx="21" cy="21" r="9" fill="none" stroke="var(--blue)" stroke-width="1.5"/><circle cx="21" cy="21" r="4" fill="none" stroke="var(--blue)" stroke-width="1.5"/></svg></div>
    <div class="service" style="top:259px"><h3>WHITE LABEL HOSTED PBX</h3>Interested in selling, installing, and managing<br>Hosted PBX? You came to the right place.</div>
    <div class="service-icon" style="top:261px"><svg width="42" height="42"><circle cx="21" cy="21" r="15" fill="none" stroke="var(--blue)" stroke-width="1.5"/><circle cx="21" cy="21" r="11" fill="none" stroke="var(--blue)" stroke-width="1.5"/><circle cx="21" cy="21" r="7" fill="none" stroke="var(--blue)" stroke-width="1.5"/><circle cx="21" cy="21" r="3" fill="none" stroke="var(--blue)" stroke-width="1.5"/></svg></div>

    <h2 class="abs headline"><small>REDEFINING</small><span>CLOUD COMMUNICATION</span></h2>
    <div class="abs cloud-art" role="img" aria-label="Illustration of desk phones floating in a cloud"></div>
  </div>

  <div class="feature-list feature-list--left">
    <div class="feature"><h4>AUTOMATED ATTENDANTS</h4>Automatically greet callers and route them anywhere.<br>Easily customizable through the web portal.</div>
    <div class="feature"><h4>CALL CENTER</h4>Setup call queues for offices with longer than normal hold times.<br>Comes with detailed reporting.</div>
    <div class="feature"><h4>MOBILE TWINNING</h4>Simultaneously ring your cell phone with your desk phone.</div>
    <div class="feature"><h4>SMARTPHONE APP</h4>Make and receive calls on the road just like you are in the office.</div>
  </div>
  <div class="feature-list feature-list--right" style="top:340px">
    <div class="feature"><h4>CONFERENCE BRIDGES</h4>Hold password protected, multi-party conference calls.</div>
    <div class="feature"><h4>MUSIC ON HOLD</h4>Use our standard music on hold or upload your own.</div>
    <div class="feature"><h4>WEB PORTAL WITH CHAT</h4>Chat with coworkers, see if they are on the phone, view your call<br>history or make system changes right from our easy to use portal.</div>
    <div class="feature"><h4>VOICEMAIL TO EMAIL</h4>Have voicemails delivered right to your email, complete with<br>caller id, .wav file, and a full text transcription of the voicemail.</div>
  </div>

  <div class="contact-band contact-band--cyan"><span>corvalink.com</span><span>|</span><span>855.CORVAL1</span><span>|</span><span>sales@corvalink.com</span></div>
  <div class="footer-strip" role="img" aria-label="Faded photo of glass office towers"></div>
</section>

</body>
</html>
```